Business Card and Stationary Design

After the successful redesign of our logo we are wanting to follow suite and create a new business card and stationary design!

New Logo is attached, information required on the business card should contain a mixture of the following but layout/arrangement is up to the designer.

Happy if the national provider number and abn are on the back, and happy for them to be smaller than the rest.

I am also happy to receive single sided or weird and wonderful designs.

Name
Title
National Provider Number 7291
ABN 53 219 864 317
Level 3, 42 Marlow Street
Carrow Vale NSW 2391
Ph: 1300 987 214
Mobile: 0432 785 619
name@ferngatebuild.com.au
www.ferngatebuild.com.au

Target Market(s)

Professionals, Peers, Students, Suppliers...

Industry/Entity Type

Construction

Contact Information for Business Card

Listed in project description

Font styles to use
Other font styles liked:
• Century Gothic

Colors
0455a3
3176b5
ffffff

Requirements
Must have
• Professional Design, same color scheme as our logo
Nice to have
• Something that sets our apart from everyone else would be fantastic, open to size and shape and layout options, as long as they present professionally.
• Open to raised/embossed text, alternative materials, custom sizes, clear material
Should not have
• The color orange

```html
<!DOCTYPE html>
<html lang="en">
<head>
<meta charset="utf-8">
<title>Ferngate Build – Business Card</title>
<link href="https://fonts.googleapis.com/css2?family=Questrial&display=swap" rel="stylesheet">
<style>
  :root {
    --brand-blue: #0455a3;
    --card-blue: #1e4596;
    --accent-blue: #3176b5;
    --ink: #1f3f86;
    --muted: #5a6f9c;
    --white: #ffffff;
    --backdrop: #e8eaee;
  }
  * { box-sizing: border-box; margin: 0; padding: 0; }
  html, body { width: 1200px; height: 900px; overflow: hidden; }
  body {
    background: var(--backdrop);
    font-family: "Questrial", "Century Gothic", sans-serif;
    display: flex;
    align-items: center;
    justify-content: center;
    gap: 60px;
  }
  .card {
    position: relative;
    width: 510px;
    height: 312px;
    box-shadow: 0 6px 18px rgba(0,0,0,0.18);
    overflow: hidden;
  }

  /* Front – contact side */
  .card--front { background: var(--white); color: var(--ink); }
  .side-band {
    position: absolute; left: 0; top: 0; bottom: 0; width: 58px;
    background: var(--card-blue);
  }
  .side-band__tab {
    position: absolute; left: 58px; top: 0; width: 30px; height: 40px;
    background: var(--card-blue);
  }
  .brand {
    position: absolute; left: 100px; top: 10px;
    display: flex; align-items: center; gap: 10px;
  }
  .brand__mark { width: 14px; height: 14px; background: var(--accent-blue); }
  .brand__name { font-size: 27px; color: var(--brand-blue); letter-spacing: 0.5px; }

  .contacts {
    position: absolute; left: 78px; top: 68px;
    list-style: none; font-size: 13.5px; line-height: 21px;
  }
  .contacts li { display: flex; align-items: center; gap: 10px; }
  .contacts svg { width: 12px; height: 12px; flex: none; fill: var(--muted); }
  .contacts .address-line2 { padding-left: 22px; }

  .person {
    position: absolute; right: 36px; top: 82px;
    text-align: right; padding-right: 14px;
    border-right: 5px solid var(--card-blue);
  }
  .person__name { font-size: 21px; color: var(--ink); line-height: 1.1; }
  .person__title { font-size: 15px; color: var(--muted); }

  .registration {
    position: absolute; left: 78px; top: 224px;
    font-size: 11.5px; color: var(--ink);
  }
  .registration span + span { margin-left: 12px; }
  .rule {
    position: absolute; left: 58px; right: 60px; top: 250px;
    height: 2px; background: var(--card-blue);
  }

  /* Back – brand side */
  .card--back {
    background: linear-gradient(160deg, #2750a3 0%, var(--card-blue) 55%, #1a3d88 100%);
    color: var(--white);
    display: flex; align-items: center; justify-content: center;
  }
  .card--back .brand { position: static; gap: 14px; }
  .card--back .brand__mark { width: 22px; height: 22px; background: var(--white); }
  .card--back .brand__name { font-size: 44px; color: var(--white); }
</style>
</head>
<body>

  <section class="card card--front" aria-label="Business card front">
    <div class="side-band"></div>
    <div class="side-band__tab"></div>

    <div class="brand">
      <span class="brand__mark"></span>
      <span class="brand__name">ferngatebuild</span>
    </div>

    <ul class="contacts">
      <li>
        <svg viewBox="0 0 12 12"><path d="M2 1h3l1 3-2 1a7 7 0 0 0 3 3l1-2 3 1v3a1 1 0 0 1-1 1A10 10 0 0 1 1 2a1 1 0 0 1 1-1z"/></svg>
        Ph: 1300 987 214
      </li>
      <li>
        <svg viewBox="0 0 12 12"><path d="M3 0h6a1 1 0 0 1 1 1v10a1 1 0 0 1-1 1H3a1 1 0 0 1-1-1V1a1 1 0 0 1 1-1zm0 2v7h6V2zm3 8a.7.7 0 1 0 0 1.4A.7.7 0 0 0 6 10z"/></svg>
        Mobile: 0432 785 619
      </li>
      <li>
        <svg viewBox="0 0 12 12"><path d="M0 2h12v8H0zm1 1v.4l5 3.3 5-3.3V3zm0 1.6V9h10V4.6L6 8z"/></svg>
        name@ferngatebuild.com.au
      </li>
      <li>
        <svg viewBox="0 0 12 12"><path d="M6 0a6 6 0 1 0 0 12A6 6 0 0 0 6 0zm0 1c.8 0 1.6 1.6 1.8 4H4.2C4.4 2.6 5.2 1 6 1zM4.2 7h3.6C7.6 9.4 6.8 11 6 11S4.4 9.4 4.2 7zM1.1 5h2.1c.1-1.4.4-2.6.9-3.4A5 5 0 0 0 1.1 5zm7.7 0h2.1a5 5 0 0 0-3-3.4c.5.8.8 2 .9 3.4zM1.1 7a5 5 0 0 0 3 3.4c-.5-.8-.8-2-.9-3.4zm7.7 0c-.1 1.4-.4 2.6-.9 3.4a5 5 0 0 0 3-3.4z"/></svg>
        www.ferngatebuild.com.au
      </li>
      <li>
        <svg viewBox="0 0 12 12"><path d="M6 0a4 4 0 0 0-4 4c0 3 4 8 4 8s4-5 4-8a4 4 0 0 0-4-4zm0 2.5a1.5 1.5 0 1 1 0 3 1.5 1.5 0 0 1 0-3z"/></svg>
        Level 3, 42 Marlow Street
      </li>
      <li class="address-line2">Carrow Vale NSW 2391</li>
    </ul>

    <div class="person">
      <p class="person__name">Your Name</p>
      <p class="person__title">your title</p>
    </div>

    <p class="registration">
      <span>National Provider Number 7291</span>
      <span>ABN 53 219 864 317</span>
    </p>
    <div class="rule"></div>
  </section>

  <section class="card card--back" aria-label="Business card back">
    <div class="brand">
      <span class="brand__mark"></span>
      <span class="brand__name">ferngatebuild</span>
    </div>
  </section>

</body>
</html>
```